Booklet Cover Design Project

Booklet cover designs - I have uploaded a couple of examples of previous covers - they should match these in concept!.

4 covers using the same theme :

1
Work Health and Safety (Medical)
KTRNPL647

2. Maintain Patient Records
KTRGOF528

3. Prepare and Process Medical Accounts
KTRGOF529

4. Confidentiality, Privacy and Security in a Medical Office
KTRGOF586

** I have uploaded a couple of samples from previous work - please use a similar style for consistency. Suggested photo samples attached.

• Consistency of theme

```html
<!DOCTYPE html>
<html lang="en">
<head>
<meta charset="utf-8">
<title>Work Health and Safety (Medical) – Learner Guide Cover</title>
<link href="https://fonts.googleapis.com/css2?family=Cormorant+SC:wght@500;600&family=Cinzel:wght@600;700&display=swap" rel="stylesheet">
<style>
  :root {
    --navy: #2c3e5c;
    --gold: #d7a94a;
    --gold-line: #d9b25f;
    --paper: #ffffff;
    --ink-dark: #33363d;
    --photo-deep: #24477a;
    --photo-mid: #4f78ad;
    --photo-light: #b9c7d6;
    --heart: #d8242b;
  }
  * { margin: 0; padding: 0; box-sizing: border-box; }
  html, body {
    width: 848px; height: 1200px; overflow: hidden; background: var(--paper);
  }
  .cover {
    position: relative; width: 848px; height: 1200px; background: var(--paper);
    font-family: "Cormorant SC", "Times New Roman", serif;
  }
  .institute {
    position: absolute; top: 128px; left: 0; width: 100%;
    display: flex; flex-direction: column; align-items: center; gap: 14px;
  }
  .institute__mark {
    width: 18px; height: 18px; background: var(--navy);
  }
  .institute__name {
    font-family: "Cinzel", Georgia, serif; font-weight: 600; font-size: 17px;
    letter-spacing: 1.5px; color: var(--navy); text-align: center; line-height: 1.3;
  }
  .title {
    position: absolute; top: 350px; left: 0; width: 100%; text-align: center;
    font-weight: 500; font-size: 42px; letter-spacing: 1px; color: var(--navy);
  }
  .subtitle {
    position: absolute; top: 412px; left: 0; width: 100%; text-align: center;
    font-weight: 600; font-size: 27px; color: var(--navy); letter-spacing: 0.5px;
  }
  .subtitle__code { color: var(--gold); font-family: "Cormorant SC", serif; }
  .hero-photo {
    position: absolute; top: 461px; left: 0; width: 848px; height: 579px;
    background:
      radial-gradient(ellipse 90px 80px at 432px 298px, var(--heart) 0%, var(--heart) 70%, rgba(216,36,43,0) 100%),
      radial-gradient(ellipse 320px 260px at 420px 300px, rgba(220,225,232,0.55), rgba(220,225,232,0) 70%),
      linear-gradient(135deg, #6d6f76 0%, var(--photo-mid) 30%, var(--photo-deep) 60%, #3b5f93 80%, #707680 100%);
  }
  .credit-band {
    position: absolute; top: 1040px; left: 0; width: 100%; height: 80px; background: var(--paper);
    display: flex; align-items: center; justify-content: center; gap: 14px;
  }
  .credit-band__rule { width: 72px; height: 1.5px; background: var(--gold-line); }
  .credit-band__text {
    font-family: "Cinzel", Georgia, serif; font-weight: 700; font-size: 17px;
    letter-spacing: 1.4px; color: var(--ink-dark);
  }
  .footer-photo {
    position: absolute; top: 1120px; left: 0; width: 848px; height: 80px;
    background: linear-gradient(90deg, #5d83b8 0%, var(--photo-deep) 45%, #3d66a0 70%, var(--photo-light) 100%);
  }
</style>
</head>
<body>
  <div class="cover">
    <header class="institute">
      <div class="institute__name">HARROWGATE INSTITUTE<br>OF TRAINING</div>
      <div class="institute__mark"></div>
    </header>

    <h1 class="title">Work Health and Safety</h1>
    <p class="subtitle">(medical) <span class="subtitle__code">KTRNPL647</span></p>

    <div class="hero-photo" role="img" aria-label="Healthcare worker in blue scrubs and gloves holding a red heart with a padlock symbol, surrounded by glowing medical and help icons"></div>

    <div class="credit-band">
      <span class="credit-band__rule"></span>
      <span class="credit-band__text">Written and compiled by Mara Fenwick</span>
      <span class="credit-band__rule"></span>
    </div>

    <div class="footer-photo" role="img" aria-label="Continuation of the blue medical photograph with a stethoscope"></div>
  </div>
</body>
</html>
```